Logo/stationary needed for a Holding Company

Hello I need a logo for my holding company, Millbrook Holdings, LLC. I would like it VERY clean and professional. I am thinking similar to a law firm or financial company. I would appreciate stationary/envelope as well under the address below. Thank you very much.

2738 East 47th Street
Crest Level
Lakemont, Illinois 60491

Target Market(s)

Irrelevant for this project

Industry/Entity Type

It Company

Logo Text

Millbrook Holdings, LLC or Millbrook Holdings

Logo styles of interest
Wordmark Logo
Lettermark Logo
Font styles to use
Serif
Sans Serif

Colors
0293ce
0355a3
3277b5
34a7d8
85cae6
85acd3
cee9f5

Requirements
Must have
• company name
Nice to have
• just very clean and professional
Should not have
• n/a

```html
<!DOCTYPE html>
<html lang="en">
<head>
<meta charset="utf-8">
<title>Millbrook Holdings — Stationery</title>
<link rel="stylesheet" href="https://fonts.googleapis.com/css2?family=Cinzel:wght@400;600&family=PT+Sans:wght@400&display=swap">
<style>
  :root {
    --backdrop: #575757;
    --paper: #ffffff;
    --envelope: #eeeef1;
    --brand-blue: #1b5aa7;
    --ink: #3a3a3a;
    --muted: #555555;
    --white: #ffffff;
  }
  * { box-sizing: border-box; margin: 0; padding: 0; }
  html, body { width: 947px; height: 1200px; overflow: hidden; }
  body { background: var(--backdrop); position: relative; font-family: "PT Sans", sans-serif; color: var(--ink); }

  .wordmark { font-family: "Cinzel", serif; font-weight: 600; color: var(--brand-blue); line-height: 1.05; text-align: center; letter-spacing: 0.04em; }
  .wordmark span { display: block; }
  .small-caps { font-family: "Cinzel", serif; font-weight: 400; }

  /* Letterhead */
  .letterhead { position: absolute; left: 40px; top: 40px; width: 560px; height: 725px; background: var(--paper); }
  .letterhead .wordmark { position: absolute; left: 36px; top: 52px; font-size: 21px; }
  .letter { position: absolute; left: 90px; right: 62px; top: 185px; font-size: 10.5px; line-height: 1.42; }
  .letter .recipient { margin-bottom: 44px; }
  .letter p { text-align: justify; margin-bottom: 13px; }
  .letter .closing { margin-top: 4px; margin-bottom: 66px; }
  .letterhead .footer-address { position: absolute; left: 0; right: 0; bottom: 20px; text-align: center; font-size: 10.5px; color: var(--muted); }
  .letterhead .footer-bar { position: absolute; left: 0; right: 0; bottom: 0; height: 13px; background: var(--brand-blue); }

  /* Business card front */
  .card { position: absolute; width: 277px; height: 158px; }
  .card-front { left: 630px; top: 40px; background: var(--paper); }
  .card-front .wordmark { position: absolute; left: 16px; top: 54px; font-size: 13px; }
  .card-front .contact { position: absolute; left: 130px; top: 40px; color: #222; }
  .card-front .name { font-size: 11px; font-weight: 600; }
  .card-front .role { font-size: 8.5px; color: var(--brand-blue); margin-bottom: 12px; }
  .card-front .address { font-size: 8.5px; line-height: 1.35; }
  .card-front .phone { font-family: "Cinzel", serif; font-size: 12px; margin-top: 6px; }
  .card-front .card-band { position: absolute; left: 0; right: 0; bottom: 0; height: 14px; background: var(--brand-blue); }

  /* Business card back */
  .card-back { left: 630px; top: 218px; background: var(--brand-blue); }
  .card-back .wordmark { position: absolute; left: 0; right: 0; top: 60px; font-size: 17px; color: var(--white); }

  /* Envelope */
  .envelope { position: absolute; left: 40px; top: 795px; width: 867px; height: 377px; background: var(--envelope); }
  .envelope .return { position: absolute; left: 40px; top: 44px; text-align: center; }
  .envelope .wordmark { font-size: 18px; margin-bottom: 10px; }
  .envelope .address { font-size: 11px; line-height: 1.4; color: var(--muted); }
</style>
</head>
<body>

  <section class="letterhead">
    <div class="wordmark"><span>Millbrook</span><span>Holdings</span></div>
    <div class="letter">
      <div class="recipient">Mr. Daniel Reyes<br>Managing Director<br>Prairie Capital Partners</div>
      <p>Lorem Ipsum is simply dummy text of the printing and typesetting industry. Lorem Ipsum has been the industry's standard dummy text ever since the 1500s, when an unknown printer took a galley of type and scrambled it to make a type specimen book. It has suvived not only five centuries, but also the leap into electronic typesetting, remaining essentially unchanged. It was popularised in the 1960s with the release of sheets containing Lorem Ipsum passages, and more recently with desktop publishing software like Folio Layout.</p>
      <p>Contrary to popular belief, Lorem Ipsum is not simply random text. It has roots in a piece of classical Latin literature from 45 BC, making it over 2000 years old. Thomas Avery, a Latin professor at a college in Virginia, looked up one of the most of the obscure Latin words and discovered the undoubtable sorce. Lorem Ipsum comes from sections 1.10.32 and 1.10.33 of "de Finibus Bonorum et Molorum" (The Extreme of Good and Evil), written in 45 BC. This book is a treatise on the theory of ethics very popular during Renaissance.</p>
      <p class="closing">Thank you for being one of our valued customers.</p>
      <div class="signature">Name Here<br>CEO</div>
    </div>
    <div class="footer-address small-caps">2738 East 47th Street | Crest Level | Lakemont, Illinois 60491</div>
    <div class="footer-bar"></div>
  </section>

  <section class="card card-front">
    <div class="wordmark"><span>Millbrook</span><span>Holdings</span></div>
    <div class="contact small-caps">
      <div class="name">Evan Whitcombe</div>
      <div class="role">Lead Team</div>
      <div class="address">2738 East 47th Street<br>Crest Level<br>Lakemont, Illinois 60491</div>
      <div class="phone">630-555-0142</div>
    </div>
    <div class="card-band"></div>
  </section>

  <section class="card card-back">
    <div class="wordmark"><span>Millbrook</span><span>Holdings</span></div>
  </section>

  <section class="envelope">
    <div class="return">
      <div class="wordmark"><span>Millbrook</span><span>Holdings</span></div>
      <div class="address small-caps">2738 East 47th Street<br>Crest Level<br>Lakemont, Illinois 60491</div>
    </div>
  </section>

</body>
</html>
```